Trevanix Template Refresh 2017

We want software development managers to remember that presentations using this template showcased Trevanix technology: Our template must be distinctive to be remembered as showing Trevanix technology: They must stand out from the 100s of other tech presentations they see, without being 'wacky', but professional whether bold or subtle. We are targeting the world's largest corporations.

[What do we do?] Trevanix offers the world's first objective, fair measure of software developer productivity (Trevanix Build Gauge) and code quality (Trevanix LUX) metrics.

Our corporate colour is (hex) Red: 13, Green: 10, Blue: 74.

Target Market(s)

CIOs, CTOs and senior software development managers in large Enterprises.

Industry/Entity Type

Information Technology

Font styles to use
Sans Serif

Colors
0355a3

Requirements
Must have
• A memorable design
Nice to have
• Template for slides that will show a view of our User Interface (which shows graphs and charts); ideally a consistent theme to make it clear that this is our own UI, not general graphs and charts to illustrate the presentation. (None of the graphs and charts in the attached presentation are from our User Interface)
• A suggestion would be to make use of our "chord" shape (cut off circle in our logo). This could be white on a blue to appear as a cut-out window for the slide content.
Should not have
• A colourful / jokey / fun tone.

```html
<!DOCTYPE html>
<html lang="en">
<head>
<meta charset="utf-8">
<title>Trevanix Template Refresh 2017</title>
<link href="https://fonts.googleapis.com/css2?family=Mulish:wght@300;400;600;700;800&display=swap" rel="stylesheet">
<style>
:root{
  --navy:#0d0a4a;
  --brand-blue:#0355a3;
  --slate:#5a6680;
  --slate-light:#8e97ab;
  --grey-text:#9aa0ab;
  --body-text:#333;
  --board:#e3e3e3;
  --paper:#fff;
  --chart-blue:#2a7fc1;
  --chart-red:#8b0b0b;
  --chart-green:#2e8b3e;
  --accent-green:#a6dc3c;
  --accent-orange:#f08a24;
}
*{box-sizing:border-box;margin:0;padding:0}
html,body{width:1200px;height:772px;overflow:hidden}
body{background:var(--board);font-family:'Mulish',Arial,sans-serif;color:var(--body-text);position:relative}
.slide{position:absolute;width:380px;height:237px;background:var(--paper);box-shadow:0 1px 4px rgba(0,0,0,.25);overflow:hidden}
.abs{position:absolute}
.slide-head{position:absolute;left:0;top:10px;height:10px;display:flex;align-items:center}
.slide-head::before{content:"";width:10px;height:10px;background:var(--navy);margin-right:9px}
.slide-head b{font-size:11px;font-weight:800;color:var(--navy);margin-right:3px}
.slide-head span{font-size:11px;font-weight:300;color:var(--grey-text)}
.page-no{position:absolute;right:0;top:10px;display:flex;align-items:center;font-size:4px;color:var(--grey-text)}
.page-no::after{content:"";width:8px;height:10px;background:var(--navy);margin-left:4px}
.footer-brand{position:absolute;bottom:4px;left:50%;transform:translateX(-50%);font-size:7.5px;font-weight:600;color:var(--navy);letter-spacing:.4px}
.kicker{font-size:9px;font-weight:300;color:var(--slate-light)}
.title{font-size:12px;font-weight:700;color:var(--slate)}
.rule{height:2px;width:28px;background:var(--slate-light)}
.para{font-size:5px;line-height:1.55;color:#444;text-align:justify}
.band{position:absolute;height:12px;background:var(--slate);display:flex}
.band div{flex:1;color:#fff;font-size:5.2px;display:flex;align-items:center;justify-content:center;border-right:1px solid #fff}
.band div:last-child{border-right:0}
.icon-dot{position:absolute;border-radius:50%;display:flex;align-items:center;justify-content:center}

/* slide 1 */
.cover-scene{position:absolute;left:0;top:0;width:380px;height:214px;background:linear-gradient(100deg,#e9e6e1 0%,#f4f2ee 35%,#d8cfc3 60%,#c9b79f 100%)}
.cover-bar{position:absolute;left:0;bottom:0;width:380px;height:23px;background:#111;display:flex;justify-content:center;align-items:center;gap:32px}
.cover-bar i{width:7px;height:7px;border-radius:50%;background:#cfcfcf;display:block}
.cover-mark{position:absolute;left:0;top:98px;width:22px;height:22px;background:var(--navy)}
.cover-brand{position:absolute;left:34px;top:99px}
.cover-brand .name{font-size:17px;font-weight:600;color:var(--navy);letter-spacing:.6px;line-height:1}
.cover-brand .tag{font-size:6px;color:var(--slate);margin-top:3px;letter-spacing:.2px}
.cover-info h3{font-size:9px;font-weight:800;color:var(--navy);line-height:1}
.cover-info p{font-size:4.6px;line-height:1.25;color:var(--navy)}

/* slide 2 */
.agenda{position:absolute;display:flex;gap:10px}
.agenda .num{font-size:20px;font-weight:300;color:#a9adb5;width:22px;line-height:1;margin-top:2px}
.agenda .item{border-left:1px solid #bbb;padding-left:4px}
.agenda .time{font-size:6px;color:var(--navy)}
.agenda .head{font-size:5.8px;font-weight:800;color:var(--navy)}
.agenda .desc{font-size:4.6px;color:var(--grey-text);margin-top:4px;line-height:1.3}

/* slide 7 */
.use-col{position:absolute;top:100px;width:58px;font-size:3.7px;line-height:1.4;color:#555;text-align:justify}
.band-sm div{font-size:3.5px;line-height:1.15;text-align:center;flex-direction:column}

/* slide 9 */
.kpi{position:absolute;text-align:center;color:var(--slate-light)}
.kpi b{display:block;font-size:11px;font-weight:600}
.kpi span{font-size:5px}
</style>
</head>
<body>

<!-- Row 1 -->
<section class="slide" style="left:10px;top:10px">
  <div class="cover-scene" role="img" aria-label="Softly blurred bright office interior with chairs and window light"></div>
  <div class="cover-mark"></div>
  <div class="cover-brand">
    <div class="name">Trevanix</div>
    <div class="tag">objective engineering insight</div>
  </div>
  <div class="cover-info abs" style="left:170px;top:102px">
    <h3>Address</h3>
    <p>48 Orchard Row, Kelby Vale<br>Northam<br>12345</p>
  </div>
  <div class="cover-info abs" style="left:260px;top:102px">
    <h3>Contact</h3>
    <p>Phone : 1-555-0142<br>Email: support@trevanix.com</p>
  </div>
  <div class="cover-bar"><i></i><i></i><i></i></div>
</section>

<section class="slide" style="left:411px;top:10px">
  <div class="slide-head"><b>Content</b><span>At Glance</span></div>
  <div class="page-no">2</div>
  <div class="agenda" style="left:36px;top:64px;flex-direction:column;gap:7px">
    <div style="display:flex;gap:8px"><div class="num">1.</div><div class="item"><div class="time">08.00 – 09.00 AM</div><div class="head">Praesent malesuada</div><div class="desc">Donec dapibus mi eu eros dictum<br>congue tempus</div></div></div>
    <div style="display:flex;gap:8px"><div class="num">2.</div><div class="item"><div class="time">08.00 – 09.00 AM</div><div class="head">Praesent malesuada</div><div class="desc">Donec dapibus mi eu eros dictum<br>congue tempus</div></div></div>
    <div style="display:flex;gap:8px"><div class="num">3.</div><div class="item"><div class="time">08.00 – 09.00 AM</div><div class="head">Praesent malesuada</div><div class="desc">Donec dapibus mi eu eros dictum<br>congue tempus</div></div></div>
  </div>
  <div class="agenda" style="left:193px;top:64px;flex-direction:column;gap:7px">
    <div style="display:flex;gap:8px"><div class="num">4.</div><div class="item"><div class="time">08.00 – 09.00 AM</div><div class="head">Praesent malesuada</div><div class="desc">Donec dapibus mi eu eros dictum<br>congue tempus</div></div></div>
    <div style="display:flex;gap:8px"><div class="num">5.</div><div class="item"><div class="time">08.00 – 09.00 AM</div><div class="head">Praesent malesuada</div><div class="desc">Donec dapibus mi eu eros dictum<br>congue tempus</div></div></div>
    <div style="display:flex;gap:8px"><div class="num">6.</div><div class="item"><div class="time">08.00 – 09.00 AM</div><div class="head">Praesent malesuada</div><div class="desc">Donec dapibus mi eu eros dictum<br>congue tempus</div></div></div>
  </div>
  <div class="footer-brand">Trevanix</div>
</section>

<section class="slide" style="left:812px;top:10px">
  <div class="slide-head"><b>How</b><span>it works</span></div>
  <div class="page-no">3</div>
  <div class="icon-dot" style="left:46px;top:67px;width:90px;height:90px;background:var(--slate)">
    <svg width="26" height="30" viewBox="0 0 26 30" fill="none" stroke="#fff" stroke-width="1.6" stroke-linecap="round"><path d="M8 20c0-3-4-5-4-10a9 9 0 0 1 18 0c0 5-4 7-4 10z"/><path d="M9 23h8M10 26h6"/><path d="M13 8a3 3 0 0 1 3 3"/></svg>
  </div>
  <div class="abs" style="right:34px;top:53px;text-align:right">
    <div class="kicker">Build Gauge</div>
    <div class="title" style="margin-top:-1px">Analytics</div>
    <div class="rule" style="margin:6px 0 0 auto"></div>
  </div>
  <p class="para abs" style="right:34px;top:98px;width:128px;text-align:right;font-size:4.8px">Trevanix is a SaaS technology that objectively measures and quantifies the productivity of software developers. Trevanix is currently the only company able to do so objectively and independently of a developer's input. We eliminate the inherent subjectivity and inaccuracy that is embedded in all other current productivity metrics (Function Points, Story Points, Reporting, Burn-down Charts, CLOC, etc).</p>
  <div class="abs" style="left:38px;top:182px;width:307px;height:1.5px;background:var(--navy)"></div>
  <p class="abs" style="left:38px;top:186px;width:307px;text-align:center;font-size:7.5px;line-height:1.3;color:var(--grey-text)"><span style="color:#222">“Build Gauge</span> is a measure of the intellectual effort required to make a source file change.”</p>
  <div class="footer-brand">Trevanix</div>
</section>

<!-- Row 2 -->
<section class="slide" style="left:10px;top:268px">
  <div class="slide-head"><b>How</b><span>it works</span></div>
  <div class="page-no">4</div>
  <div class="abs" style="left:19px;top:36px">
    <div class="kicker">Calculating</div>
    <div class="title">Build Gauge</div>
    <div class="rule" style="margin-top:6px"></div>
  </div>
  <svg class="abs" style="left:0;top:60px" width="380" height="80">
    <circle cx="190" cy="19" r="16" fill="var(--slate)" stroke="#c9ccd3" stroke-width="2"/>
    <path d="M185 14l-5 5 5 5M195 14l5 5-5 5M192 12l-4 14" stroke="#fff" stroke-width="1.4" fill="none" stroke-linecap="round"/>
    <line x1="126" y1="43" x2="254" y2="43" stroke="#999" stroke-width=".6" stroke-dasharray="1 1"/>
    <line x1="190" y1="35" x2="190" y2="52" stroke="#999" stroke-width=".6" stroke-dasharray="1 1"/>
    <line x1="126" y1="43" x2="126" y2="51" stroke="#999" stroke-width=".6" stroke-dasharray="1 1"/>
    <line x1="254" y1="43" x2="254" y2="51" stroke="#999" stroke-width=".6" stroke-dasharray="1 1"/>
    <circle cx="126" cy="43" r="1.3" fill="#777"/><circle cx="190" cy="43" r="1.3" fill="#777"/><circle cx="254" cy="43" r="1.3" fill="#777"/>
    <circle cx="126" cy="64" r="13" fill="var(--slate)"/>
    <path d="M119 61l7-4 7 4-7 4zM119 65l7 4 7-4M119 68l7 4 7-4" stroke="#fff" stroke-width="1" fill="none"/>
    <circle cx="190" cy="64" r="13" fill="var(--slate)"/>
    <path d="M183 59h3l7 10h3M183 69h3l7-10h3M194 57l2 2-2 2M194 67l2 2-2 2" stroke="#fff" stroke-width="1" fill="none"/>
    <circle cx="254" cy="64" r="13" fill="var(--slate)"/>
    <path d="M250 64l8-5M250 64l8 5" stroke="#fff" stroke-width="1"/><circle cx="250" cy="64" r="2" fill="none" stroke="#fff"/><circle cx="258" cy="59" r="2" fill="none" stroke="#fff"/><circle cx="258" cy="69" r="2" fill="none" stroke="#fff"/>
  </svg>
  <div class="band" style="left:0;top:146px;width:380px">
    <div style="flex:0 0 94px"></div>
    <div style="flex:0 0 64px;background:var(--navy)">Volume</div>
    <div style="flex:0 0 64px;background:var(--navy)">Complexity</div>
    <div style="flex:0 0 64px;background:var(--navy)">Interrelatedness</div>
    <div></div>
  </div>
  <div class="abs" style="left:94px;top:166px;width:192px;display:grid;grid-template-columns:1fr 1fr 1fr;text-align:center;font-size:5.5px;row-gap:6px;color:#333">
    <span>SLoC</span><span>McCabe</span><span>DAC</span>
    <span>CLoC</span><span>Halstead</span><span>Fan Out</span>
  </div>
  <div class="abs" style="left:100px;top:192px;width:190px;height:.6px;background:#ccc"></div>
  <ul class="abs" style="left:120px;top:195px;font-size:4.8px;color:var(--grey-text);list-style:none;line-height:1.4">
    <li>▸ 36 static metrics evaluation per code revision</li>
    <li>▸ 360 source file types measured</li>
  </ul>
  <div class="footer-brand">Trevanix</div>
</section>

<section class="slide" style="left:411px;top:268px">
  <div class="slide-head"><b>How</b><span>it works</span></div>
  <div class="page-no">5</div>
  <div class="abs" style="left:19px;top:34px">
    <div class="kicker">Static Metric</div>
    <div class="title">Gathering</div>
    <div class="rule" style="margin-top:5px"></div>
  </div>
  <p class="para abs" style="left:19px;top:76px;width:209px">Trevanix integrates with source code repositories and task trackers, evaluating the changes between every historical revision made by each developer in terms of more than 36 static source code metrics. These metrics deliver the most holistic understanding of the intellectual effort required to make a change to a source file, evaluating three broad domains of the change. Example static metrics include:</p>
  <svg class="abs" style="left:19px;top:126px" width="209" height="24">
    <circle cx="32" cy="12" r="11" fill="#c2c6cf"/><path d="M26 10l6-3 6 3-6 3zM26 13l6 3 6-3" stroke="#fff" stroke-width=".9" fill="none"/>
    <circle cx="103" cy="12" r="11" fill="#c2c6cf"/><path d="M97 8h2l6 8h2M97 16h2l6-8h2" stroke="#fff" stroke-width=".9" fill="none"/>
    <circle cx="175" cy="12" r="11" fill="#c2c6cf"/><path d="M171 12l7-4M171 12l7 4" stroke="#fff" stroke-width=".9"/><circle cx="171" cy="12" r="1.6" fill="none" stroke="#fff"/><circle cx="178" cy="8" r="1.6" fill="none" stroke="#fff"/><circle cx="178" cy="16" r="1.6" fill="none" stroke="#fff"/>
  </svg>
  <div class="band" style="left:19px;top:155px;width:209px"><div>Volume</div><div>Complexity</div><div>Interrelatedness</div></div>
  <p class="para abs" style="left:19px;top:171px;width:209px">We detect and adjust/filter automated or repetitive changes. Categories including code generation, automatic IDE changes, copy/paste, merging &amp; branching, automated refactoring.</p>
  <div class="abs" style="left:271px;top:72px;width:89px;height:90px;border-radius:10px;background:var(--slate);display:flex;align-items:center;justify-content:center">
    <svg width="34" height="28" viewBox="0 0 34 28" fill="none" stroke="#fff" stroke-width="1.5"><path d="M3 26h28"/><path d="M6 25v-6M11 25v-9M16 25v-6M21 25v-10M26 25v-14" stroke-width="3"/><path d="M4 16l8-6 5 4 12-10"/><path d="M25 4h5v5"/></svg>
  </div>
  <div class="footer-brand">Trevanix</div>
</section>

<section class="slide" style="left:812px;top:268px">
  <div class="slide-head"><b>How</b><span>it works</span></div>
  <div class="page-no">6</div>
  <svg class="abs" style="left:20px;top:60px" width="170" height="160">
    <path d="M58 42a32 32 0 0 1 8-20" fill="none" stroke="#b8bcc6" stroke-width="3"/>
    <path d="M62 16l8 4-6 5z" fill="#b8bcc6"/>
    <path d="M22 104a34 34 0 0 1 0-28" fill="none" stroke="#b8bcc6" stroke-width="3"/>
    <path d="M17 102l9 0-4 7z" fill="#b8bcc6"/>
    <path d="M135 68a52 52 0 0 1 8 88" fill="none" stroke="var(--navy)" stroke-width="3.5"/>
    <path d="M136 158l8 4 2-9z" fill="var(--navy)"/>
    <circle cx="75" cy="32" r="24" fill="var(--slate)"/>
    <text x="75" y="30" fill="#fff" font-size="5.5" text-anchor="middle">Code</text>
    <text x="75" y="37" fill="#fff" font-size="5.5" text-anchor="middle">Delivered</text>
    <circle cx="100" cy="102" r="39" fill="var(--navy)"/>
    <circle cx="44" cy="73" r="28" fill="#b8bcc6"/>
    <text x="44" y="75" fill="#fff" font-size="5.5" text-anchor="middle">Work Context</text>
    <text x="100" y="104" fill="#fff" font-size="6" text-anchor="middle">Build Gauge</text>
  </svg>
  <div class="abs" style="left:198px;top:63px">
    <div class="title">Benchmarking</div>
    <div class="rule" style="margin-top:4px"></div>
  </div>
  <p class="para abs" style="left:198px;top:92px;width:148px;font-size:4.9px">Every code change is benchmarked and placed on a multidimensional continuum. Trevanix then calculates a Build Gauge score, representing the amount of time it would take your average developer to make a change. Time and Motion studies show a correlation of ~0.85 with Build Gauge hours to accurately time tracked developers.</p>
  <div class="footer-brand">Trevanix</div>
</section>

<!-- Row 3 -->
<section class="slide" style="left:10px;top:526px">
  <div class="slide-head"><b>Cost Savings –</b><span>High Level Use Cases</span></div>
  <div class="page-no">7</div>
  <div class="abs" style="left:72px;top:41px;font-size:8px;color:#222">Quick Wins</div>
  <div class="abs" style="left:246px;top:41px;font-size:8px;color:#222">Long Term Goals</div>
  <div class="abs" style="left:0;top:55px;width:380px;height:.6px;background:#ccc"></div>
  <svg class="abs" style="left:0;top:57px" width="380" height="20" fill="none" stroke="#8e97ab" stroke-width="1.1" stroke-linecap="round">
    <path d="M30 16l10-10 4 0 0 4-10 10zM32 12l-3-1M36 16l1 3"/>
    <rect x="89" y="5" width="10" height="11" rx="3"/><path d="M91 5l1-3h4l1 3M91 16l1 3h4l1-3M94 8v3h2"/>
    <path d="M146 6l-4 5 4 5M158 6l4 5-4 5M154 4l-4 14"/>
    <path d="M227 8a6 6 0 1 0 1 5M227 4v4h-4"/>
    <path d="M276 6h3l6 9h3M276 15h3l6-9h3M286 4l2 2-2 2M286 13l2 2-2 2"/>
    <path d="M331 9l5-3 4 2 4-2 5 3-5 6-4 2-5-3zM336 6l3 5"/>
  </svg>
  <div class="band band-sm" style="left:0;top:78px;width:380px;height:12px">
    <div style="flex:0 0 10px"></div>
    <div>Improve under utilized<br>resources (Capacity save)</div>
    <div>Time to Productivity<br>(Capacity save)</div>
    <div>Cost of Missing<br>Developers (Cash save)</div>
    <div>% change before or after<br>UAT (Capacity save)</div>
    <div>Vendor Onshore/ Offshore<br>(Cash save)</div>
    <div>Vendor / Deal Type<br>(Cash save)</div>
  </div>
  <p class="use-col" style="left:13px">Underutilized resources are quickly identified and the root cause analysis of reasons for this underutilization is easily established, rectified and tracked across teams, so capacity returns to delivery within one review cycle.</p>
  <p class="use-col" style="left:76px">Onboarding processes are measured so new starters reach productive output sooner; managers compare ramp-up speed across sites, tune mentoring and documentation, and prove the gain in recovered capacity each quarter.</p>
  <p class="use-col" style="left:139px">Missing developers are detected through steady effort records, showing who is not delivering against plan; addressing these gaps releases budget that can be redeployed to achieving teams with clear evidence.</p>
  <p class="use-col" style="left:202px">With objective data to hand, managers can see the real cost of late defects and compare effort before and after acceptance testing, moving quality checks earlier where they pay back most.</p>
  <p class="use-col" style="left:265px">Migration of development roles from high cost to low cost locations is judged on delivered output rather than headcount, so onshore and offshore choices rest on comparable measures of productive work.</p>
  <p class="use-col" style="left:317px;width:56px">Vendors and deal types are compared with a single objective view of output per unit of cost, giving procurement a fair basis to renegotiate terms, reward strong suppliers and plan future contracts with confidence.</p>
  <div class="footer-brand">Trevanix</div>
</section>

<section class="slide" style="left:411px;top:526px">
  <div class="slide-head"><b>Monthly</b><span>Trend</span></div>
  <div class="page-no">8</div>
  <svg class="abs" style="left:14px;top:48px;border:1px solid #ddd" width="268" height="148" font-size="2.6" fill="#555">
    <text x="140" y="3.5" text-anchor="middle">Date</text>
    <text x="50" y="7">2014 Q4</text><text x="120" y="7">Q1</text><text x="170" y="7">2015 Q2</text><text x="235" y="7">Q3</text>
    <text x="8" y="36" transform="rotate(-90 8 36)" text-anchor="middle">Productivity</text>
    <text x="8" y="88" transform="rotate(-90 8 88)" text-anchor="middle">Cost per Hour</text>
    <text x="8" y="128" transform="rotate(-90 8 128)" text-anchor="middle">Developers</text>
    <line x1="14" y1="10" x2="14" y2="138" stroke="#ccc" stroke-width=".5"/>
    <g fill="var(--chart-blue)">
      <rect x="18" y="26" width="15" height="32"/><rect x="38" y="27" width="15" height="31"/><rect x="58" y="27" width="15" height="31"/><rect x="78" y="26" width="15" height="32"/><rect x="98" y="28" width="15" height="30"/><rect x="118" y="27" width="15" height="31"/><rect x="138" y="27" width="15" height="31"/><rect x="158" y="28" width="15" height="30"/><rect x="178" y="25" width="15" height="33"/><rect x="198" y="27" width="15" height="31"/><rect x="218" y="22" width="15" height="36"/><rect x="238" y="18" width="15" height="40"/>
    </g>
    <g fill="var(--chart-red)">
      <rect x="18" y="80" width="15" height="30"/><rect x="38" y="81" width="15" height="29"/><rect x="58" y="79" width="15" height="31"/><rect x="78" y="80" width="15" height="30"/><rect x="98" y="76" width="15" height="34"/><rect x="118" y="72" width="15" height="38"/><rect x="138" y="70" width="15" height="40"/><rect x="158" y="72" width="15" height="38"/><rect x="178" y="77" width="15" height="33"/><rect x="198" y="75" width="15" height="35"/><rect x="218" y="80" width="15" height="30"/><rect x="238" y="78" width="15" height="32"/>
    </g>
    <g fill="var(--chart-green)">
      <rect x="18" y="108" width="15" height="30"/><rect x="38" y="119" width="15" height="19"/><rect x="58" y="119" width="15" height="19"/><rect x="78" y="120" width="15" height="18"/><rect x="98" y="121" width="15" height="17"/><rect x="118" y="122" width="15" height="16"/><rect x="138" y="122" width="15" height="16"/><rect x="158" y="121" width="15" height="17"/><rect x="178" y="121" width="15" height="17"/><rect x="198" y="121" width="15" height="17"/><rect x="218" y="120" width="15" height="18"/><rect x="238" y="120" width="15" height="18"/>
    </g>
    <g text-anchor="middle">
      <text x="25" y="142">Oct</text><text x="45" y="142">Nov</text><text x="65" y="142">Dec</text><text x="85" y="142">Jan</text><text x="105" y="142">Feb</text><text x="125" y="142">Mar</text><text x="145" y="142">Apr</text><text x="165" y="142">May</text><text x="185" y="142">Jun</text><text x="205" y="142">Jul</text><text x="225" y="142">Aug</text><text x="245" y="142">Sep</text>
    </g>
  </svg>
  <p class="abs" style="left:14px;top:197px;width:268px;font-size:2.8px;line-height:1.25;color:#666">Caption&nbsp;&nbsp;This view gives a strategic picture of how the organisation is changing over time. The blue row shows average productivity per person. The red row shows cost per hour of effort. The green row shows active developers.</p>
  <div class="abs" style="left:287px;top:48px;width:83px;height:148px;background:var(--navy)">
    <svg class="abs" style="left:27px;top:25px" width="30" height="24" viewBox="0 0 34 28" fill="none" stroke="#fff" stroke-width="1.5"><path d="M3 26h28"/><path d="M6 25v-6M11 25v-9M16 25v-6M21 25v-10M26 25v-14" stroke-width="3"/><path d="M4 16l8-6 5 4 12-10"/><path d="M25 4h5v5"/></svg>
    <div class="abs" style="left:0;top:78px;width:83px;height:.6px;background:#fff"></div>
    <p class="abs" style="left:4px;top:82px;width:75px;font-size:5px;line-height:1.35;color:#fff;text-align:justify">In <b>Q3 average productivity</b> per person (blue) is trending up as cost per hour of effort delivered (red) trends down. The organisation is becoming more performing.</p>
  </div>
  <div class="footer-brand">Trevanix</div>
</section>

<section class="slide" style="left:812px;top:526px">
  <div class="slide-head"><b>Dashboard</b><span>Sample</span></div>
  <div class="page-no">9</div>
  <div class="kpi" style="left:18px;top:50px;width:52px"><b>1,400</b><span>Sales Revenue</span></div>
  <div class="kpi" style="left:18px;top:79px;width:52px"><b>17,500</b><span>Total Revenue</span></div>
  <svg class="abs" style="left:100px;top:36px" width="270" height="98" font-size="4.5" fill="#777">
    <g stroke="#e2e2e2" stroke-width=".5">
      <line x1="51" y1="6" x2="51" y2="86"/><line x1="85" y1="6" x2="85" y2="86"/><line x1="119" y1="6" x2="119" y2="86"/><line x1="153" y1="6" x2="153" y2="86"/><line x1="187" y1="6" x2="187" y2="86"/><line x1="221" y1="6" x2="221" y2="86"/><line x1="255" y1="6" x2="255" y2="86"/>
    </g>
    <line x1="17" y1="4" x2="17" y2="86" stroke="#aaa" stroke-width=".5"/>
    <line x1="17" y1="86" x2="258" y2="86" stroke="#aaa" stroke-width=".5"/>
    <g text-anchor="end"><text x="14" y="88">0</text><text x="14" y="80">10</text><text x="14" y="72">20</text><text x="14" y="64">30</text><text x="14" y="56">40</text><text x="14" y="48">50</text><text x="14" y="40">60</text><text x="14" y="32">70</text><text x="14" y="24">80</text><text x="14" y="16">90</text><text x="14" y="8">100</text></g>
    <g text-anchor="middle"><text x="17" y="94">0</text><text x="51" y="94">2</text><text x="85" y="94">4</text><text x="119" y="94">6</text><text x="153" y="94">8</text><text x="187" y="94">10</text><text x="221" y="94">12</text><text x="255" y="94">14</text></g>
    <polyline points="34,78 51,74 68,70 85,65.2 102,59.6 119,50 136,46 153,46 170,32.4 187,38 204,30 221,14" fill="none" stroke="var(--slate)" stroke-width="1"/>
    <g fill="#fff" stroke="#e0634a" stroke-width=".8">
      <circle cx="34" cy="78" r="1.6"/><circle cx="51" cy="74" r="1.6"/><circle cx="68" cy="70" r="1.6"/><circle cx="85" cy="65.2" r="1.6"/><circle cx="102" cy="59.6" r="1.6"/><circle cx="119" cy="50" r="1.6"/><circle cx="136" cy="46" r="1.6"/><circle cx="153" cy="46" r="1.6"/><circle cx="170" cy="32.4" r="1.6"/><circle cx="187" cy="38" r="1.6"/><circle cx="204" cy="30" r="1.6"/><circle cx="221" cy="14" r="1.6"/>
    </g>
    <g text-anchor="middle" font-size="4.2"><text x="34" y="74">10</text><text x="51" y="70">15</text><text x="68" y="66">20</text><text x="85" y="61">26</text><text x="102" y="55">33</text><text x="119" y="46">45</text><text x="136" y="42">50</text><text x="153" y="42">50</text><text x="170" y="28">67</text><text x="187" y="34">60</text><text x="204" y="26">70</text><text x="221" y="10">90</text></g>
  </svg>
  <div class="abs" style="left:0;top:147px;width:380px;height:90px;background:var(--navy)">
    <div class="abs" style="left:16px;top:5px;font-size:5.5px;color:#fff">Phasellus maximus mauris at pulvinar mollis.</div>
    <svg class="abs" style="left:6px;top:14px" width="220" height="72" font-size="4" fill="#fff">
      <g text-anchor="end"><text x="12" y="6">150</text><text x="12" y="24">100</text><text x="12" y="42">50</text><text x="12" y="60">0</text></g>
      <line x1="14" y1="3" x2="14" y2="58" stroke="#fff" stroke-width=".5"/>
      <line x1="14" y1="58" x2="216" y2="58" stroke="#fff" stroke-width=".5"/>
      <rect x="20" y="18" width="6" height="40" fill="#e8542c"/>
      <rect x="36" y="22" width="6" height="36" fill="#f5b800"/>
      <rect x="52" y="46" width="6" height="12" fill="#a6dc3c"/>
      <rect x="68" y="22" width="6" height="36" fill="#2e9e3e"/>
      <rect x="84" y="18" width="6" height="40" fill="#28a8e0"/>
      <rect x="100" y="40" width="6" height="18" fill="#8e97ab"/>
      <rect x="116" y="44" width="6" height="14" fill="#f08a24"/>
      <rect x="132" y="30" width="6" height="28" fill="#f5d000"/>
      <rect x="148" y="50" width="6" height="8" fill="#a6dc3c"/>
      <rect x="164" y="38" width="6" height="20" fill="#2e9e3e"/>
      <rect x="180" y="18" width="6" height="40" fill="#28a8e0"/>
      <rect x="196" y="42" width="6" height="16" fill="#8e97ab"/>
      <g text-anchor="middle"><text x="23" y="66">Jan</text><text x="39" y="66">Feb</text><text x="55" y="66">Mar</text><text x="71" y="66">Apr</text><text x="87" y="66">May</text><text x="103" y="66">Jun</text><text x="119" y="66">Jul</text><text x="135" y="66">Aug</text><text x="151" y="66">Sep</text><text x="167" y="66">Act</text><text x="183" y="66">Nov</text><text x="199" y="66">Dec</text></g>
    </svg>
    <div class="abs" style="left:240px;top:17px;font-size:5.5px;color:#fff">ANNUAL REPORT</div>
    <div class="abs" style="left:312px;top:8px;width:57px;height:28px;background:var(--accent-green);color:var(--navy);font-size:11px;font-weight:600;display:flex;align-items:center;justify-content:center">17,500</div>
    <div class="abs" style="left:236px;top:44px;width:134px;height:.6px;background:#fff"></div>
    <div class="abs" style="left:242px;top:53px;font-size:8.5px;color:var(--accent-orange)">$ 17,500,000</div>
    <div class="abs" style="left:242px;top:67px;font-size:5px;color:#fff">Phasellus maximus mauris.</div>
    <div class="abs" style="left:332px;top:53px;width:23px;height:20px;background:#2fbf5a;display:flex;align-items:center;justify-content:center">
      <svg width="10" height="10" viewBox="0 0 10 10"><path d="M2 1l7 4-7 4z" fill="#fff"/></svg>
    </div>
  </div>
</section>

</body>
</html>
```